Flyer

I am a qualified accountant and I need a flyer to promote my business when networking

My services include
Management Accounts, Financial Accounts, Day to Day Bookkeeping services, business start up assistance
I will produce and submit Self Assessment Tax Returns, Annual Accounts, VAT tax returns, Payroll and PAYE

I attach my business card design so that there is some continuity if you think it appropiate.

Size A3 is preferred, please.

Sorry, I mean't Size A5 is preferred.

A5 please

Free initial consultations and advice.

```html
<!DOCTYPE html>
<html lang="en">
<head>
<meta charset="utf-8">
<title>Clara Webb Accounting – Business Services</title>
<link rel="stylesheet" href="https://fonts.googleapis.com/css2?family=Carlito:ital,wght@0,400;0,700;1,700&display=swap">
<style>
  :root {
    --green-dark: #1d7a35;
    --green-text: #1e6e2e;
    --green-light: #b9d43a;
    --ink: #111111;
    --white: #ffffff;
    --photo-light: #eef3f8;
    --photo-mid: #b9c9da;
    --photo-deep: #6f86a3;
  }
  * { margin: 0; padding: 0; box-sizing: border-box; }
  html, body { width: 846px; height: 1200px; overflow: hidden; background: var(--white); }
  body { font-family: "Carlito", "Calibri", Arial, sans-serif; }
  .flyer { position: relative; width: 846px; height: 1200px; overflow: hidden; background: var(--white); }

  .top-wave { position: absolute; top: 0; left: 0; width: 846px; height: 90px; }

  .brand { position: absolute; top: 84px; left: 460px; width: 410px; text-align: center; }
  .brand-name { font-weight: 700; font-size: 36px; line-height: 46px; color: var(--ink); letter-spacing: 0.5px; }
  .brand-tagline { margin-top: 6px; font-size: 23px; color: var(--ink); letter-spacing: 0.3px; }

  .team-icon { position: absolute; left: 158px; top: 232px; width: 138px; height: 130px; border-radius: 50% 50% 22px 22px;
    background: radial-gradient(circle at 35% 40%, #5a93d6, #2f6fb8 55%, #8fbf4a 100%); opacity: 0.9; }

  .services-badge { position: absolute; left: 310px; top: 224px; width: 380px; height: 154px; border-radius: 50%;
    background: var(--green-light); display: flex; align-items: center; justify-content: center; text-align: center;
    font-weight: 700; font-style: italic; font-size: 41px; line-height: 46px; color: var(--ink); letter-spacing: 0.5px; }

  .service-list { position: absolute; left: 124px; top: 394px; list-style: none; }
  .service-list li { position: relative; padding-left: 45px; font-weight: 700; font-style: italic; font-size: 32px;
    line-height: 44px; color: var(--green-text); }
  .service-list .tick { position: absolute; left: 0; top: 13px; width: 22px; height: 20px; }

  .offer-badge { position: absolute; left: 552px; top: 676px; width: 246px; height: 200px; border-radius: 50%;
    background: var(--green-light); transform: rotate(-8deg); display: flex; flex-direction: column;
    align-items: center; justify-content: center; text-align: center; color: var(--green-text); font-weight: 700; }
  .offer-badge .offer-free { font-size: 44px; line-height: 44px; color: #23331c; }
  .offer-badge .offer-free small { font-size: 26px; color: var(--green-text); }
  .offer-badge .offer-text { font-size: 27px; line-height: 34px; }

  .photo { position: absolute; left: 0; top: 850px; width: 846px; height: 300px; }

  .contact-bar { position: absolute; left: 0; bottom: 0; width: 846px; height: 50px; background: var(--green-dark);
    color: var(--white); font-weight: 700; font-size: 20px; display: flex; align-items: center; justify-content: center;
    letter-spacing: 0.3px; }
</style>
</head>
<body>
<main class="flyer">
  <svg class="top-wave" viewBox="0 0 846 90" aria-hidden="true">
    <path d="M0 0 H846 V22 C700 6 560 14 420 40 C300 62 170 72 0 50 Z" fill="#1d7a35"/>
    <path d="M0 58 C170 80 300 70 420 48 C560 22 700 14 846 30" fill="none" stroke="#b9d43a" stroke-width="5"/>
  </svg>

  <header class="brand">
    <div class="brand-name">CLARA WEBB<br>ACCOUNTING</div>
    <div class="brand-tagline">MAKING ACCOUNTS LOOK EASY</div>
  </header>

  <div class="team-icon" role="img" aria-label="Icon of two business people with a gear"></div>

  <div class="services-badge">BUSINESS<br>SERVICES</div>

  <ul class="service-list">
    <li><svg class="tick" viewBox="0 0 22 20"><path d="M2 11 L8 17 L20 2" fill="none" stroke="#1e6e2e" stroke-width="2.5"/></svg>Management Accounts</li>
    <li><svg class="tick" viewBox="0 0 22 20"><path d="M2 11 L8 17 L20 2" fill="none" stroke="#1e6e2e" stroke-width="2.5"/></svg>Financial Accounts</li>
    <li><svg class="tick" viewBox="0 0 22 20"><path d="M2 11 L8 17 L20 2" fill="none" stroke="#1e6e2e" stroke-width="2.5"/></svg>Day to Day Book&nbsp; Keeping Services</li>
    <li><svg class="tick" viewBox="0 0 22 20"><path d="M2 11 L8 17 L20 2" fill="none" stroke="#1e6e2e" stroke-width="2.5"/></svg>Business Start Up Assistance</li>
    <li><svg class="tick" viewBox="0 0 22 20"><path d="M2 11 L8 17 L20 2" fill="none" stroke="#1e6e2e" stroke-width="2.5"/></svg>Can Produce And Submit Self<br>Assessment&nbsp; Tax Returns</li>
    <li><svg class="tick" viewBox="0 0 22 20"><path d="M2 11 L8 17 L20 2" fill="none" stroke="#1e6e2e" stroke-width="2.5"/></svg>Annual Accounts</li>
    <li><svg class="tick" viewBox="0 0 22 20"><path d="M2 11 L8 17 L20 2" fill="none" stroke="#1e6e2e" stroke-width="2.5"/></svg>VAT tax returns</li>
    <li><svg class="tick" viewBox="0 0 22 20"><path d="M2 11 L8 17 L20 2" fill="none" stroke="#1e6e2e" stroke-width="2.5"/></svg>Payroll</li>
    <li><svg class="tick" viewBox="0 0 22 20"><path d="M2 11 L8 17 L20 2" fill="none" stroke="#1e6e2e" stroke-width="2.5"/></svg>PAYE</li>
  </ul>

  <div class="offer-badge">
    <div class="offer-free">FREE <small>Initial</small></div>
    <div class="offer-text">Consultations<br>And Advice</div>
  </div>

  <svg class="photo" viewBox="0 0 846 300" role="img" aria-label="Photo of business people reviewing financial charts at a desk">
    <defs>
      <linearGradient id="photoTone" x1="0" y1="0" x2="1" y2="1">
        <stop offset="0" stop-color="#b9c9da"/>
        <stop offset="0.45" stop-color="#eef3f8"/>
        <stop offset="1" stop-color="#6f86a3"/>
      </linearGradient>
    </defs>
    <path d="M0 20 C250 0 560 0 846 12 V300 H0 Z" fill="url(#photoTone)"/>
  </svg>

  <footer class="contact-bar">EMAIL: clara@clarawebbaccounting.com CONTACT # 07700 900123</footer>
</main>
</body>
</html>
```